Harbor Crest Solutions Letterhead Design

The project name sums it up. Just need a professional letterhead design / template we can use in our marketing folders.

Here's the address / contact info for the letterhead: Harbor Crest Solutions 4817 Maple Ridge Dr Suite 150 League City, Texas 77419 346-508-7364 www.harborcrestsolutions.us support@harborcrestsolutions.us

```html
<!DOCTYPE html>
<html lang="en">
<head>
<meta charset="UTF-8">
<title>Harbor Crest Solutions Letterhead</title>
<link rel="stylesheet" href="https://fonts.googleapis.com/css2?family=Roboto:wght@300;400;700&family=Pinyon+Script&display=swap">
<style>
  :root {
    --canvas: #e4e4e4;
    --paper: #f2f2f2;
    --ink: #2a2a2a;
    --muted: #6b6b6b;
    --brand-blue: #1a4ba0;
    --brand-dark: #1b1b1b;
    --bar-dark: #626262;
    --bar-light: #cfcfcf;
  }
  * { margin: 0; padding: 0; box-sizing: border-box; }
  html, body { width: 1200px; height: 1200px; overflow: hidden; }
  body {
    background: var(--canvas);
    font-family: "Roboto", Arial, sans-serif;
    color: var(--ink);
    position: relative;
  }
  .letterhead {
    position: absolute;
    left: 204px;
    top: 40px;
    width: 792px;
    height: 1120px;
    background: var(--paper);
    box-shadow: 0 4px 18px rgba(0,0,0,0.12);
    overflow: hidden;
  }
  .brand {
    position: absolute;
    left: 52px;
    top: 66px;
    display: flex;
    align-items: center;
    gap: 12px;
  }
  .brand-mark {
    width: 44px;
    height: 44px;
    border-radius: 50%;
    background: var(--brand-blue);
  }
  .brand-name {
    font-weight: 700;
    font-size: 21px;
    color: var(--brand-dark);
    letter-spacing: 0.3px;
  }
  .contact {
    position: absolute;
    right: 49px;
    top: 43px;
    text-align: right;
    font-size: 13px;
    font-weight: 400;
    color: var(--muted);
    line-height: 16px;
  }
  .contact .address { margin-bottom: 5px; }
  .contact-line {
    display: flex;
    justify-content: flex-end;
    align-items: center;
    gap: 7px;
  }
  .contact-line svg { width: 10px; height: 10px; flex: none; }
  .accent-bar {
    position: absolute;
    right: 0;
    top: 46px;
    width: 10px;
    height: 96px;
    background: var(--brand-blue);
  }
  .letter {
    position: absolute;
    left: 85px;
    top: 264px;
    width: 623px;
    font-size: 12.6px;
    font-weight: 300;
    line-height: 18.6px;
    color: var(--ink);
  }
  .letter .date { margin-bottom: 18px; }
  .letter .recipient { margin-bottom: 37px; }
  .letter .salutation { margin-bottom: 18px; }
  .letter .body p { text-align: justify; margin-bottom: 18.6px; }
  .letter .closing { margin-top: 44px; }
  .letter .signature {
    font-family: "Pinyon Script", cursive;
    font-size: 24px;
    line-height: 34px;
    color: var(--ink);
    margin-top: 4px;
  }
  .footer-bar {
    position: absolute;
    left: 0;
    bottom: 0;
    width: 100%;
    height: 13px;
    background: linear-gradient(90deg, var(--bar-dark), var(--bar-light) 50%, var(--bar-dark));
  }
</style>
</head>
<body>
  <div class="letterhead">
    <div class="brand">
      <span class="brand-mark"></span>
      <span class="brand-name">Harbor Crest Solutions</span>
    </div>

    <div class="contact">
      <div class="address">
        4817 Maple Ridge Dr.<br>
        Suite 150 League City<br>
        Texas 77419
      </div>
      <div class="contact-line">346-508-7364
        <svg viewBox="0 0 10 10"><path d="M2 0.5 L3.8 2.6 L2.9 3.8 Q4 6 6.2 7.1 L7.4 6.2 L9.5 8 L8.4 9.5 Q3.5 9 0.5 1.6 Z" fill="var(--brand-blue)"/></svg>
      </div>
      <div class="contact-line">support@harborcrestsolutions.us
        <svg viewBox="0 0 10 10"><rect x="0.6" y="1.8" width="8.8" height="6.4" fill="none" stroke="var(--brand-blue)" stroke-width="1"/><path d="M0.6 1.8 L5 5.6 L9.4 1.8" fill="none" stroke="var(--brand-blue)" stroke-width="1"/></svg>
      </div>
      <div class="contact-line">www.harborcrestsolutions.us
        <svg viewBox="0 0 10 10"><circle cx="5" cy="5" r="4.4" fill="none" stroke="var(--brand-blue)" stroke-width="1"/><ellipse cx="5" cy="5" rx="1.9" ry="4.4" fill="none" stroke="var(--brand-blue)" stroke-width="0.9"/><path d="M0.6 5 H9.4 M1.3 2.8 H8.7 M1.3 7.2 H8.7" stroke="var(--brand-blue)" stroke-width="0.8"/></svg>
      </div>
    </div>
    <div class="accent-bar"></div>

    <div class="letter">
      <p class="date">01 January 2050</p>
      <p class="recipient">Company (Pvt) Ltd.<br>PO Box 3355 Mainville St<br>Sample City Country 3355</p>
      <p class="salutation">Dear Daniel Whitford,</p>
      <div class="body">
        <p>Lorem ipsum dolor sit amet, consectetuer adipiscing elit, sed diam nonummy nibh euismod tincidunt ut laoreet dolore magna aliquam erat volutpat. Ut wisi enim ad minim veniam, quis nostrud exerci tation ullamcorper suscipit lobortis nisl ut aliquip ex ea commodo consequat. Duis dolore te feugait nulla facilisi. Nam liber tempor cum soluta nobis eleifend option congue nihil imperdiet doming id quod mazim placerat facer possim assum. Lorem ipsum dolor sit amet, consectetuer adipiscing elit, sed diam nonummy nibh euismod tincidunt ut laoreet dolore magna aliquam erat volutpat. Ut wisi enim ad minim veniam, quis nostrud exerci tation ullamcorper suscipit lobortis nisl ut aliquip ex ea commodo consequat.</p>
        <p>Consectetuer adipiscing elit, sed diam nonummy nibh euismod tincidunt ut laoreet dolore magna aliquam erat volutpat. Ut wisi enim ad minim veniam, quis nostrud exerci tation ullamcorper suscipit lobortis nisl ut aliquip ex ea commodo consequat. Consectetuer adipiscing elit, sed diam nonummy nibh euismod tincidunt ut laoreet dolore magna aliquam erat volutpat. Ut wisi enim ad minim veniam, quis nostrud exerci tation ullamcorper suscipit lobortis nisl ut aliquip ex ea commodo consequat.</p>
        <p>Consectetuer adipiscing elit, sed diam nonummy nibh euismod tincidunt ut laoreet dolore magna aliquam erat volutpat. Ut wisi enim ad minim veniam, quis nostrud exerci tation ullamcorper suscipit lobortis nisl ut aliquip ex ea commodo consequat. Consectetuer adipiscing elit, sed diam nonummy nibh euismod tincidunt ut laoreet dolore magna aliquam erat volutpat. Ut wisi enim ad minim veniam, quis nostrud exerci tation ullamcorper suscipit lobortis nisl ut aliquip ex ea commodo consequat.</p>
      </div>
      <p class="closing">Sincerely Yours</p>
      <p class="signature">Thomas Albrecht</p>
    </div>

    <div class="footer-bar"></div>
  </div>
</body>
</html>
```